need a Flyer for Plush Toy company

Need a Flyer for Plush Toy company ,

I upload a file for TEXT

Target Market(s)

Toys wholesalers , Supermarket

Industry/Entity Type

Toy Store

Colors
000000
ec1f27
c4c4c4

Requirements
Must have
• I have up loaded 3 files
• 1. Logo Registered Brand
• 2. customer's design in drawing
• 3. our ready samples based on Design
Nice to have
• happy kids in Nature ,
• happy kids in Ski ,
• different color Kids ,
• Multi culture concept

```html
<!DOCTYPE html>
<html lang="en">
<head>
<meta charset="utf-8">
<title>Lumo Plush – Family Business Flyer</title>
<link rel="stylesheet" href="https://fonts.googleapis.com/css2?family=Bangers&family=Patrick+Hand&family=Arimo:wght@700&display=swap">
<style>
  :root {
    --red: #e21b23;
    --orange: #f26b21;
    --green: #8dc63f;
    --lime: #b5e08a;
    --yellow: #f3c51f;
    --navy: #1d3b6e;
    --grey: #c4c4c4;
    --paper: #f7f7f5;
    --white: #ffffff;
  }
  * { margin: 0; padding: 0; box-sizing: border-box; }
  html, body { width: 927px; height: 1200px; overflow: hidden; }
  body { background: var(--white); }
  .flyer {
    position: relative;
    width: 927px;
    height: 1200px;
    overflow: hidden;
    background: radial-gradient(ellipse at 30% 20%, #ffffff 0%, var(--paper) 70%, #ececea 100%);
    font-family: "Arimo", Arial, sans-serif;
  }
  .abs { position: absolute; }

  /* brand */
  .brand {
    left: 92px; top: 72px;
    display: flex; align-items: center; gap: 14px;
  }
  .brand-square { width: 24px; height: 24px; background: var(--red); }
  .brand-name {
    font-family: "Bangers", sans-serif;
    font-size: 84px; color: var(--red); line-height: 1;
    letter-spacing: 2px;
  }

  /* identity lines */
  .identity { left: 126px; top: 212px; font-family: "Bangers", sans-serif; }
  .identity .line-orange { color: var(--orange); font-size: 30px; letter-spacing: 1px; line-height: 34px; }
  .identity .line-green { color: var(--green); font-size: 17px; letter-spacing: .5px; line-height: 24px; display: flex; align-items: center; gap: 8px; }
  .bar { width: 22px; height: 12px; background: var(--red); transform: skewX(-25deg); }

  .arrow { left: 488px; top: 205px; }

  .ship-illustration {
    left: 590px; top: 30px; width: 290px; height: 270px;
    border-radius: 50%;
    background: radial-gradient(circle at 55% 55%, #f6d64a 0%, #f9e58f 45%, rgba(255,255,255,0) 72%);
  }

  .tagline { left: 585px; top: 292px; font-family: "Patrick Hand", cursive; font-size: 40px; color: var(--navy); }
  .place { left: 578px; top: 345px; display: flex; align-items: baseline; gap: 10px; font-family: "Bangers", sans-serif; }
  .place .city { color: var(--red); font-size: 32px; }
  .place .region { color: var(--grey); font-size: 18px; }
  .languages { left: 578px; top: 392px; display: flex; align-items: center; gap: 12px; font-family: "Bangers", sans-serif; font-size: 34px; color: var(--green); }

  .kids-photo {
    left: 228px; top: 338px; width: 262px; height: 116px;
    border-radius: 40px 40px 0 0;
    background: linear-gradient(180deg, #f3eee8 0%, #e6cdb5 55%, #c9a98a 100%);
  }

  /* dark story panel */
  .panel { left: 0; top: 0; }
  .skier-photo { left: 34px; top: 482px; width: 64px; height: 82px; border-radius: 10px; background: linear-gradient(160deg, #9fb3c8, #4a5866); }
  .toys-photo {
    left: 120px; top: 770px; width: 740px; height: 200px;
    background: radial-gradient(ellipse at 50% 80%, rgba(240,200,120,.35), rgba(0,0,0,0) 70%);
  }

  .story { font-weight: 700; color: var(--white); white-space: nowrap; line-height: 1; }
  .story .l { position: absolute; font-size: 22px; }
  .story .s { position: absolute; font-size: 19.5px; }
  .story .green { color: var(--lime); }
  .story .red { color: var(--red); }
  .story .yellow { color: var(--yellow); }

  /* footer */
  .bank { left: 30px; top: 1042px; font-family: "Bangers", sans-serif; font-size: 19px; color: #3b3b3b; letter-spacing: .6px; line-height: 22px; }
  .address { left: 360px; top: 1036px; font-family: "Bangers", sans-serif; font-size: 16px; color: var(--red); letter-spacing: .5px; }
  .sofa-illustration {
    left: 366px; top: 1062px; width: 254px; height: 112px;
    border-radius: 28px 28px 14px 14px;
    background: linear-gradient(180deg, #f2f2f2 0%, #c7e6b0 55%, #8fcf85 100%);
  }
  .contact { left: 652px; top: 1040px; font-family: "Bangers", sans-serif; font-size: 19px; color: #6a6a6a; letter-spacing: .6px; line-height: 22.5px; }
</style>
</head>
<body>
<main class="flyer">

  <svg class="abs" style="left:0;top:0" width="927" height="1200" aria-hidden="true">
    <ellipse cx="150" cy="1100" rx="190" ry="95" fill="#ffffff"/>
    <ellipse cx="480" cy="1110" rx="170" ry="90" fill="#ffffff"/>
    <ellipse cx="790" cy="1100" rx="180" ry="100" fill="#ffffff"/>
  </svg>

  <div class="abs brand">
    <span class="brand-square"></span>
    <span class="brand-name">LUMO PLUSH</span>
  </div>

  <div class="abs identity">
    <div class="line-orange">EINZELUNTERNEHMEN</div>
    <div class="line-orange">FAMILY BUSINESS</div>
    <div class="line-green">INNOVATIVE DEVELOPER&nbsp; FOR PLUSH TOYS</div>
    <div class="line-green"><span class="bar"></span>INTERNATIONAL TRADER FOR TOYS</div>
  </div>

  <svg class="abs arrow" width="112" height="48" viewBox="0 0 112 48" aria-hidden="true">
    <polygon points="0,24 36,0 36,14 112,14 112,34 36,34 36,48" fill="var(--red)"/>
  </svg>

  <div class="abs ship-illustration" role="img" aria-label="Illustration of two plush toy pirates sailing a small ship"></div>

  <div class="abs tagline">Have you been there?</div>

  <div class="abs place">
    <svg width="26" height="34" viewBox="0 0 26 34" aria-hidden="true">
      <path d="M13 2C7 2 2.5 6.5 2.5 12.5 2.5 20 13 32 13 32S23.5 20 23.5 12.5C23.5 6.5 19 2 13 2Z" fill="none" stroke="#333" stroke-width="2.5"/>
      <circle cx="13" cy="12.5" r="4" fill="none" stroke="#333" stroke-width="2.5"/>
    </svg>
    <span class="city">BERGHEIM</span>
    <span class="region">COLOGNE, GERMANY</span>
  </div>

  <div class="abs languages">
    <svg width="30" height="30" viewBox="0 0 30 30" aria-hidden="true">
      <g fill="none" stroke="#333" stroke-width="2.2">
        <circle cx="15" cy="15" r="12.5"/>
        <ellipse cx="15" cy="15" rx="5.5" ry="12.5"/>
        <line x1="2.5" y1="15" x2="27.5" y2="15"/>
        <line x1="5" y1="8" x2="25" y2="8"/>
        <line x1="5" y1="22" x2="25" y2="22"/>
      </g>
    </svg>
    <span>GERMAN &amp; ENGLISH</span>
  </div>

  <div class="abs kids-photo" role="img" aria-label="Photo of three happy children lying on the floor"></div>

  <svg class="abs panel" width="927" height="1200" aria-hidden="true">
    <defs>
      <linearGradient id="panelFill" x1="0" y1="0" x2="0" y2="1">
        <stop offset="0" stop-color="#141414"/>
        <stop offset=".5" stop-color="#242424"/>
        <stop offset=".75" stop-color="#8a8580"/>
        <stop offset="1" stop-color="#d9d6d2"/>
      </linearGradient>
    </defs>
    <polygon points="150,456 880,456 876,988 72,976 110,600" fill="url(#panelFill)"/>
  </svg>

  <div class="abs skier-photo" role="img" aria-label="Small photo of a child skiing in the snow"></div>
  <div class="abs toys-photo" role="img" aria-label="Photo of colourful sample plush toys: chicks, a lion and a pig"></div>

  <div class="abs story" style="left:0;top:0;">
    <span class="l" style="left:222px;top:480px">We live and work in Bergheim near to Cologne</span>
    <span class="l" style="left:205px;top:510px">Germany. We speak <span class="green">German and English</span>.</span>
    <span class="l" style="left:179px;top:553px">The toys are made in China, we are small family</span>
    <span class="l" style="left:179px;top:583px">business , but we are professional in <span class="red">Plush toys</span></span>
    <span class="l" style="left:179px;top:613px">business , right now we have successfully</span>
    <span class="l" style="left:303px;top:647px">launched Projects with a <span class="yellow">huge</span></span>
    <span class="l" style="left:353px;top:677px"><span class="yellow">Japanese 100 Yen Chain Store</span>.</span>
    <span class="l" style="left:401px;top:707px">Here in Flyer we show a Sample</span>
    <span class="l" style="left:179px;top:737px">project.</span>
    <span class="s" style="left:179px;top:784px">100 Yen = 0.90 USD&nbsp; . Our products can meet</span>
    <span class="s" style="left:179px;top:814px">strictest <span class="red">Quality Control</span> , but are with extremely <span class="yellow">Low</span></span>
    <span class="s" style="left:179px;top:844px"><span class="yellow">Price</span> to fit for&nbsp; Japanese Dollar Shop as well as his</span>
    <span class="s" style="left:179px;top:874px">overseas Store around the world.</span>
    <span class="s" style="left:155px;top:924px">Of course our products are fit for&nbsp; Premium Store too.</span>
  </div>

  <div class="abs bank">
    BANK INFORMATION :<br>
    KONTOINHABER/ACCOUNT HOLDER:&nbsp;&nbsp; MEI LIN<br>
    IBAN:&nbsp; DE00 1234 5678 9012 3456 78<br>
    BIC : ABCDDEFF000
  </div>

  <div class="abs address">LINDENWEG 8, 50126 BERGHEIM GERMANY</div>
  <div class="abs sofa-illustration" role="img" aria-label="Illustration of plush animal toys sitting on a green sofa"></div>

  <div class="abs contact">
    HELLO@LUMOPLUSH.DE<br>
    FON&nbsp; +49 (0) 2271- 400 1100<br>
    FAX&nbsp; +49 (0) 2271- 400 1101<br>
    MOBIL: +49 (0) 151 0000 123<br>
    UST-IDNR./VAT NO. DE000111222
  </div>

</main>
</body>
</html>
```